Web Design Project For Hot Tub Company [DETAILED instructions inside with a VIDEO!!]

Site will be aimed at individual consumers and not business owners. The purpose of the site is NOT to sell hot tubs online, but to entice people to come to the actual store.

According to the client, it is mostly MEN who initiate contact, while the WOMEN come into the store. This means, the design elements should appeal to MEN more so than to WOMEN.

Right now, the clients only web presence is this Brindle Listings ad:

-LINK-
http://www.brindlelistings.example/albuquerque-nm/mip/spa-shop-albuquerque-813274605
-

Site layout will include an area for a large video on the top, below the menu bar. There will be NO optin form on this site, so there will be some open space next to the video. Be creative and use it to highlight something unique about the business (they pride themselves on their high-end products, low monthly maintenance fees, and after purchase care-the company offers FREE delivery, installation, training, 2 free "drain and fills" and a 30-exchange guarantee.) with an interesting graphic.

Below that, a standard FOUR column layout with images and text that can be hyperlinked later to interior pages. Interior pages will include a sidebar. Below that, a standard footer.

Navigation will include the following: Home, About Us, Models, After Market Service, Testimonials, , and Contact Us.

Ideally, this company's site should appeal to higher income couples without children, new homeowners, and wealthy families.

Company's Logo is attached

Target Market(s)

Upper middle class to upper class families-boyfriends, husbands and fathers mostly.

Industry/Entity Type

Business

Requirements
Must have
• -Area for a video player
-Fun, inviting layout that will appeal to upper middle class husbands and boyfriends.
Nice to have
• *Creativity!!!!

A website with a header, a horizontal navigation bar, a video, a four column layout, and a footer are pretty common and standard. Use your creativity to stay within our parameters without looking like a boring, cookie-cutter website.

Though the site should appeal to men, do not exclude women.
Should not have
• *An optin form

```html
<!DOCTYPE html>
<html lang="en">
<head>
<meta charset="utf-8">
<title>Spa Shop Albuquerque</title>
<link rel="stylesheet" href="https://fonts.googleapis.com/css2?family=Lobster+Two:ital,wght@0,400;0,700;1,400;1,700&family=Lora:ital,wght@1,600&display=swap">
<style>
:root{
  --teal:#1d8fa8;
  --teal-dark:#0e6f86;
  --ink:#3a3a3a;
  --muted:#8a8a8a;
  --paper:#f4f4f4;
  --white:#ffffff;
  --footer:#0b3b44;
  --footer-deep:#082d35;
  --footer-text:#2f8da0;
  --water-light:#8fd6d8;
  --water-mid:#49b4bd;
  --water-deep:#2a8f9c;
}
*{box-sizing:border-box;margin:0;padding:0}
html,body{width:964px;height:1200px;overflow:hidden;background:var(--white)}
body{position:relative;font-family:"Lobster Two",cursive;color:var(--ink)}
.abs{position:absolute}

/* header */
.topbar{left:0;top:0;width:964px;height:63px;background:linear-gradient(#fbfbfb,#eeeeee)}
.brand{left:112px;top:0;width:184px;height:128px;background:var(--white);border-radius:0 0 10px 10px;box-shadow:0 2px 6px rgba(0,0,0,.25);text-align:center;z-index:3}
.brand-mark{display:block;margin:22px auto 6px;width:20px;height:20px;border-radius:50%;background:var(--teal)}
.brand-name{font-size:24px;line-height:28px;color:var(--teal);font-weight:400}
.nav{right:103px;top:20px;display:flex;gap:23px;font-size:17px;font-weight:700;font-style:italic;color:var(--ink)}
.nav .active{color:var(--teal)}

/* video */
.video{left:0;top:63px;width:964px;height:394px;background:radial-gradient(ellipse at 55% 45%,#3fa7c0 0%,#2b6f80 18%,#6b4a30 45%,#2a1d15 100%)}
.play-big{left:445px;top:219px;width:79px;height:53px;border-radius:8px;background:rgba(20,20,20,.85)}
.controls{left:72px;top:440px;width:816px;height:14px}
.ctrl-btn{top:0;width:16px;height:14px;border-radius:2px}
.ctrl-play{left:0;background:#f2f2f2}
.ctrl-close{left:801px;background:#3c6d80}
.track{left:28px;top:4px;width:766px;height:6px;border-radius:3px;background:#d8eef5}
.track-fill{left:0;top:0;width:185px;height:6px;border-radius:3px;background:linear-gradient(#5fc8ea,#1b8fbf)}

/* welcome */
.welcome-title{left:177px;top:485px;font-size:22px;font-weight:700;font-style:italic;color:#555}
.welcome-text{left:378px;top:484px;width:405px;font-size:12.5px;line-height:19px;font-style:italic;font-weight:700;color:#555}
.brace{left:358px;top:480px}

/* water */
.water{left:0;top:640px;width:964px;height:344px;background:linear-gradient(180deg,var(--water-light) 0%,var(--water-mid) 45%,var(--water-deep) 100%)}

/* cards */
.cards{left:110px;top:547px;width:744px;height:200px;background:var(--paper);border-radius:4px;box-shadow:0 1px 4px rgba(0,0,0,.2);display:flex;padding:12px 12px 0 12px}
.card{flex:1;padding:0 10px 0 10px;border-right:1px dashed #c8c8c8;display:flex;flex-direction:column;align-items:center}
.card:first-child{padding-left:0}
.card:last-child{border-right:0;padding-right:0}
.card-photo{width:166px;height:82px;border:3px solid var(--white);box-shadow:0 0 0 1px #cfcfcf;border-radius:3px}
.card-title{margin-top:6px;font-size:17px;font-weight:700;font-style:italic;color:var(--teal);display:flex;align-items:center;gap:8px}
.card-title::before,.card-title::after{content:"";width:28px;height:1px;background:#888}
.card-text{margin-top:4px;width:166px;font-family:"Lora",serif;font-style:italic;font-weight:600;font-size:11px;line-height:17px;text-align:justify;color:#333}
.more{color:var(--teal);font-family:"Lobster Two",cursive;font-weight:700;float:right}

/* features */
.features{left:110px;top:764px;width:371px;height:190px;background:var(--paper);border-radius:4px;box-shadow:0 1px 4px rgba(0,0,0,.2);padding:12px 14px}
.features h2{font-size:17px;font-weight:700;font-style:italic;color:var(--teal-dark);padding:0 0 8px 2px;border-bottom:1px dashed #c8c8c8;margin-right:0}
.features ul{list-style:none;margin-top:6px}
.features li{font-size:12.5px;font-style:italic;font-weight:700;color:#444;line-height:25.5px;padding-left:18px;position:relative}
.features li::before{content:"";position:absolute;left:0;top:12px;width:10px;height:1px;background:#999}

/* footer */
.footer{left:0;top:984px;width:964px;height:181px;background:var(--footer)}
.footer-links{left:118px;top:1006px;list-style:none;width:130px}
.footer-links li{font-size:13.5px;font-weight:700;font-style:italic;color:var(--footer-text);height:24px;line-height:24px;border-bottom:1px dotted rgba(47,141,160,.35);padding-left:16px;position:relative}
.footer-links li::before{content:"";position:absolute;left:2px;top:9px;border-left:5px solid var(--footer-text);border-top:3px solid transparent;border-bottom:3px solid transparent}
.contact{left:566px;top:1008px;font-size:13.5px;font-weight:700;font-style:italic;color:var(--footer-text)}
.contact-row{display:flex;align-items:center;gap:10px;height:24px}
.rule{left:568px;top:1068px;width:250px;height:1px;background:rgba(47,141,160,.3)}
.follow{left:570px;top:1082px;font-size:13.5px;font-weight:700;font-style:italic;color:var(--footer-text)}
.social{left:572px;top:1109px;display:flex;gap:7px}
.social span{width:23px;height:23px;border-radius:4px}
.bottombar{left:0;top:1165px;width:964px;height:35px;background:var(--footer-deep)}
.copyright{right:118px;top:1176px;font-size:10.5px;font-style:italic;color:#2a6f7d}
</style>
</head>
<body>
<header>
  <div class="abs topbar"></div>
  <div class="abs brand">
    <span class="brand-mark"></span>
    <div class="brand-name">Spa Shop<br>Albuquerque</div>
  </div>
  <nav class="abs nav">
    <span class="active">Home</span><span>About Us</span><span>Models</span><span>After Market Service</span><span>Testimonials</span><span>Contact Us</span>
  </nav>
</header>

<section class="abs video" role="img" aria-label="Video still: a couple relaxing in a lit hot tub surrounded by candles"></section>
<svg class="abs play-big" viewBox="0 0 79 53" aria-hidden="true"><rect width="79" height="53" rx="8" fill="#1a1a1a" opacity=".85"/><path d="M33 16 L50 26.5 L33 37Z" fill="#4fb3d6"/></svg>
<div class="abs controls">
  <svg class="abs ctrl-btn ctrl-play" viewBox="0 0 16 14" aria-hidden="true"><rect width="16" height="14" rx="2" fill="#f2f2f2"/><path d="M6 4 L11 7 L6 10Z" fill="#666"/></svg>
  <div class="abs track"><div class="abs track-fill"></div></div>
  <svg class="abs ctrl-btn ctrl-close" viewBox="0 0 16 14" aria-hidden="true"><rect width="16" height="14" rx="2" fill="#3c6d80"/><path d="M5 4 L11 10 M11 4 L5 10" stroke="#cfe6ee" stroke-width="1.5"/></svg>
</div>

<section>
  <h1 class="abs welcome-title">Welcome to our site</h1>
  <svg class="abs brace" width="14" height="44" viewBox="0 0 14 44" aria-hidden="true"><path d="M12 2 C5 2 7 18 2 22 C7 26 5 42 12 42" fill="none" stroke="#aaa" stroke-width="1.5"/></svg>
  <p class="abs welcome-text">Lorem ipsum dolor sit amet, consectetur adipisicing elit, sed do eiusmod tempor incididunt eiusmod tempor ut labore et dolore magna aliqua.</p>
</section>

<div class="abs water" role="img" aria-label="Photo of clear turquoise pool water with a woman floating"></div>

<section class="abs cards">
  <article class="card">
    <div class="card-photo" role="img" aria-label="Photo of people in an outdoor hot tub" style="background:linear-gradient(135deg,#6b8a5a,#c9d4d8 60%,#8aa0a8)"></div>
    <h3 class="card-title">Models</h3>
    <p class="card-text">Lorem ipsum dolor sit amet, consectetur adipisicing elit, sed do eiusmod tempor incididunt ut labore et dolore. <span class="more">More...</span></p>
  </article>
  <article class="card">
    <div class="card-photo" role="img" aria-label="Photo of a hand holding a business card" style="background:linear-gradient(135deg,#f2f2f2,#d9d9d9 55%,#2a2a2a)"></div>
    <h3 class="card-title">After Market Service</h3>
    <p class="card-text">Lorem ipsum dolor sit amet, consectetur adipisicing elit, sed do eiusmod tempor incididunt ut labore et dolore. <span class="more">More...</span></p>
  </article>
  <article class="card">
    <div class="card-photo" role="img" aria-label="Photo of a couple in a candlelit indoor spa" style="background:radial-gradient(ellipse at 55% 55%,#3aa3c0,#6b4a30 55%,#2a1d15)"></div>
    <h3 class="card-title">Testimonials</h3>
    <p class="card-text">Lorem ipsum dolor sit amet, consectetur adipisicing elit, sed do eiusmod tempor incididunt ut labore et dolore. <span class="more">More...</span></p>
  </article>
  <article class="card">
    <div class="card-photo" role="img" aria-label="Photo of a customer service agent with a headset" style="background:linear-gradient(135deg,#9cc3dd,#e6e9ee 50%,#c79a7a)"></div>
    <h3 class="card-title">Contact Us</h3>
    <p class="card-text">Lorem ipsum dolor sit amet, consectetur adipisicing elit, sed do eiusmod tempor incididunt ut labore et dolore. <span class="more">More...</span></p>
  </article>
</section>

<section class="abs features">
  <h2>Our unique features</h2>
  <ul>
    <li>They pride themselves on their high-end products.</li>
    <li>Low monthly maintenance fees.</li>
    <li>After purchase care-the company offers FREE delivery Installation.</li>
    <li>Training 2 free "drain and fills".</li>
    <li>30-exchange guarantee.</li>
  </ul>
</section>

<footer>
  <div class="abs footer"></div>
  <ul class="abs footer-links">
    <li>Home</li><li>About Us</li><li>Models</li><li>After Market Service</li><li>Testimonials</li><li>Contact Us</li>
  </ul>
  <div class="abs contact">
    <div class="contact-row">
      <svg width="15" height="11" viewBox="0 0 15 11" aria-hidden="true"><rect x=".5" y=".5" width="14" height="10" fill="none" stroke="#2f8da0"/><path d="M.5 .5 L7.5 6 L14.5 .5" fill="none" stroke="#2f8da0"/></svg>
      <span>2240 Larkspur Ave NE, Albuquerque, NM 87110</span>
    </div>
    <div class="contact-row">
      <svg width="15" height="15" viewBox="0 0 15 15" aria-hidden="true"><circle cx="7.5" cy="7.5" r="6.8" fill="none" stroke="#2f8da0"/><path d="M5 4 L6.5 4 L7 6 L6 6.8 C6.6 8 7.2 8.6 8.2 9 L9 8 L11 8.5 L11 10 C7.5 10.5 4.5 7.5 5 4Z" fill="#2f8da0"/></svg>
      <span>(505) 555-0148</span>
    </div>
  </div>
  <div class="abs rule"></div>
  <div class="abs follow">Follow Us :</div>
  <div class="abs social" aria-label="Social links">
    <span style="background:#3a9bc4"></span><span style="background:#3d63a8"></span><span style="background:#58b0c0"></span><span style="background:#d6972e"></span><span style="background:#cfcfcf"></span>
  </div>
  <div class="abs bottombar"></div>
  <p class="abs copyright">Copyright©2013, Spa Shop Albuquerque</p>
</footer>
</body>
</html>
```